Banner Design for Websites

I am looking for a few various banner designs of the below size. I want them to look authentic, bold and catchy.
Width 939
Height 262
Wording:
WANTED: DRIVEN AND SUCCESSFUL INDIVIDUALS READY TO TAKE THEIR RESULTS TO THE NEXT LEVEL.

Make up to $5000 per sale
No cold calling
No experience required
No pressure selling
NOT MLM

Personal Empowerment. The Next Big Business Boom !

I make well in excess of 10k per month consistently. Brenda K

Some photos attached for use and also some others banners for various workding other than above.

```html
<!DOCTYPE html>
<html lang="en">
<head>
<meta charset="utf-8">
<title>Wanted Banner</title>
<link rel="stylesheet" href="https://fonts.googleapis.com/css2?family=Open+Sans:wght@600;700;800&display=swap">
<style>
  :root {
    --black: #000000;
    --white: #ffffff;
    --red-deep: #7a1014;
    --red-mid: #b0232a;
    --red-light: #c8343a;
    --silver-dark: #6d6f72;
    --silver-light: #e9eaec;
    --button-blue: #2a6fd6;
    --button-light: #9fd2ff;
    --button-navy: #0b1d4a;
    --band-tan: #bfb39a;
    --band-text: #2a2118;
    --photo-top: #4a3a35;
    --photo-bottom: #8a6a5c;
  }
  * { margin: 0; padding: 0; box-sizing: border-box; }
  html, body { width: 1200px; height: 335px; overflow: hidden; background: var(--black); }
  body { font-family: "Open Sans", Arial, sans-serif; }

  .banner { position: relative; width: 1200px; height: 335px; overflow: hidden; }

  .headline-panel {
    position: absolute; left: 0; top: 0; width: 594px; height: 335px;
    background: var(--black);
  }
  .headline {
    position: absolute; left: 20px; top: 40px;
    color: var(--white); font-weight: 800; font-size: 35px;
    line-height: 42px; letter-spacing: 0.3px; text-transform: uppercase;
  }

  .divider {
    position: absolute; left: 594px; top: 0; width: 19px; height: 335px;
    background: linear-gradient(90deg, var(--silver-dark), var(--silver-light) 45%, var(--silver-dark));
  }

  .offer-panel {
    position: absolute; left: 613px; top: 0; width: 587px; height: 335px;
    background: radial-gradient(ellipse at 40% 45%, var(--red-light), var(--red-mid) 45%, var(--red-deep) 100%);
  }

  .benefits {
    position: absolute; left: 670px; top: 14px; list-style: none;
    color: var(--white); font-weight: 700; font-size: 19px; line-height: 22px;
  }
  .benefits li { position: relative; padding-left: 35px; margin-bottom: 4px; width: 200px; }
  .benefits .tick { position: absolute; left: 0; top: -6px; width: 30px; height: 28px; }

  .cta {
    position: absolute; left: 652px; top: 243px; width: 203px; height: 61px;
    border-radius: 16px; border: 3px solid var(--silver-light);
    background: linear-gradient(180deg, var(--button-light) 0%, var(--button-blue) 50%, #1650b4 51%, #3d8be8 100%);
    box-shadow: 0 3px 6px rgba(0,0,0,0.5);
    display: flex; align-items: center; justify-content: center;
    color: var(--button-navy); font-weight: 800; font-size: 20px; letter-spacing: 0.3px;
    text-decoration: none;
  }

  .testimonial-photo {
    position: absolute; left: 971px; top: 6px; width: 224px; height: 324px;
    background: linear-gradient(180deg, var(--photo-top), var(--photo-bottom));
  }

  .testimonial-band { position: absolute; left: 0; top: 0; width: 1200px; height: 335px; pointer-events: none; }
  .testimonial-text { font-family: "Open Sans", Arial, sans-serif; font-weight: 600; font-size: 15px; fill: var(--band-text); }
</style>
</head>
<body>
<div class="banner">
  <section class="headline-panel">
    <h1 class="headline">Wanted:<br>Driven and successful<br>individuals ready to<br>take their results to<br>the next level.</h1>
  </section>

  <div class="divider"></div>

  <section class="offer-panel"></section>

  <ul class="benefits">
    <li><svg class="tick" viewBox="0 0 30 28"><path d="M3 15 L11 23 L27 3" fill="none" stroke="#ffffff" stroke-width="4" stroke-linecap="round" stroke-linejoin="round"/></svg>Make up to $5000 per sale</li>
    <li><svg class="tick" viewBox="0 0 30 28"><path d="M3 15 L11 23 L27 3" fill="none" stroke="#ffffff" stroke-width="4" stroke-linecap="round" stroke-linejoin="round"/></svg>No cold calling</li>
    <li><svg class="tick" viewBox="0 0 30 28"><path d="M3 15 L11 23 L27 3" fill="none" stroke="#ffffff" stroke-width="4" stroke-linecap="round" stroke-linejoin="round"/></svg>No experience required</li>
    <li><svg class="tick" viewBox="0 0 30 28"><path d="M3 15 L11 23 L27 3" fill="none" stroke="#ffffff" stroke-width="4" stroke-linecap="round" stroke-linejoin="round"/></svg>No pressure selling</li>
    <li><svg class="tick" viewBox="0 0 30 28"><path d="M3 15 L11 23 L27 3" fill="none" stroke="#ffffff" stroke-width="4" stroke-linecap="round" stroke-linejoin="round"/></svg>NOT MLM</li>
  </ul>

  <a class="cta" href="#">FIND OUT HOW</a>

  <div class="testimonial-photo" role="img" aria-label="Photo of a smiling family: a woman in a red dress, a man in a blue shirt and a young girl"></div>

  <svg class="testimonial-band" viewBox="0 0 1200 335">
    <polygon points="984,335 1200,121 1200,205 1061,335" fill="var(--band-tan)"/>
    <g transform="translate(1110,262) rotate(-45)">
      <text class="testimonial-text" text-anchor="middle" y="-18">I make well in excess of</text>
      <text class="testimonial-text" text-anchor="middle" y="0">$10,000/month</text>
      <text class="testimonial-text" text-anchor="middle" y="18">consistently. Brenda K</text>
    </g>
  </svg>
</div>
</body>
</html>
```